Business Card Design for anfurniture upcycling business specialisting in rustic, provincial & alpine

I need a business card design for a new aspect of my business called Brush Of Heartland. I upcycle rustic & provincial furniture with beautiful chalk & milk paints, wax & hemp oil to create lovely looking statement pieces. I have also created a range of Alpine décor items using reclaimed wood, chalk &ints & stencils. The alpine theme is carried over into a range of cushions suitable for the alpine apartment/lodge featuring deer, antlers and the names of many key worldwide ski resorts. Small homeware items such as cheese boards &am rack hangers also feature on our web page.I do not have a design in mind or colours, but want the card to convey professionalism, creativity & maybe highlight the alpine theme more, although I do not want people to look at the card, and think that alpine themed furniture and homewares is all there is.

Reason: not happy with any of the designs submitted so far; just not coming back with anything different that fits my business

Industry/Entity Type

Business

Contact Information for Business Card

Paint Me ProvincialRustic, Provincial & Alpine Themed Furniture & HomewaresContact Marlene - 0478-222-839cwilby@ozemail.com.auwww.facenook.example.au/Brush Of Heartland

Font styles to use
Decorative

Requirements
Must have
• Business name & the types of furniture that I upcycle
• Contact details
• My furniture would be bought by people wanting something different, not the cheap (or expensive) furniture that can be bought anywhere; but by people that want something different in their life
Nice to have
• maybe something that incorporates the three areas I do
Should not have
• Generic - could be any businesses card

```html
<!DOCTYPE html>
<html lang="en">
<head>
<meta charset="UTF-8">
<title>Brush Of Heartland – Business Cards</title>
<link rel="stylesheet" href="https://fonts.googleapis.com/css2?family=Open+Sans:wght@400;600;700&family=Raleway:wght@300&display=swap">
<style>
  :root {
    --backdrop: #3f3631;
    --card: #0b0b0c;
    --blue: #1d9ad8;
    --purple: #6a2c7c;
    --grey: #6f6f72;
    --white: #f2f2f2;
    --divider: #2a3a44;
  }
  * { margin: 0; padding: 0; box-sizing: border-box; }
  html, body { width: 1200px; height: 900px; overflow: hidden; }
  body {
    background: var(--backdrop);
    font-family: "Open Sans", Arial, sans-serif;
    display: flex;
    align-items: center;
    justify-content: center;
    gap: 48px;
  }
  .card {
    width: 540px;
    height: 310px;
    background: var(--card);
    position: relative;
    box-shadow: 0 18px 40px rgba(0,0,0,.45);
  }

  /* Contact side */
  .card--contact {
    display: flex;
    align-items: center;
    padding: 0 34px;
  }
  .brand-block {
    width: 200px;
    display: flex;
    flex-direction: column;
    align-items: center;
    gap: 14px;
  }
  .brand-mark {
    width: 70px; height: 70px;
    border-radius: 50%;
    background: var(--blue);
  }
  .brand-block__name {
    color: var(--blue);
    font-weight: 700;
    font-size: 18px;
    text-align: center;
    line-height: 1.2;
  }
  .contact-block {
    border-left: 1px solid var(--divider);
    padding: 18px 0 18px 24px;
    margin-left: 16px;
  }
  .contact-block__name {
    color: var(--blue);
    font-weight: 600;
    font-size: 19px;
    margin-bottom: 14px;
  }
  .contact-list { list-style: none; }
  .contact-list li {
    display: flex;
    align-items: center;
    gap: 12px;
    color: var(--white);
    font-size: 14.5px;
    line-height: 1.75;
    white-space: nowrap;
  }
  .contact-list svg { width: 11px; height: 11px; flex: none; fill: var(--blue); }
  .social-square { width: 10px; height: 10px; background: var(--blue); flex: none; }

  /* Front side */
  .card--front {
    display: flex;
    flex-direction: column;
    align-items: center;
    justify-content: center;
    text-align: center;
  }
  .card--front .brand-mark { width: 84px; height: 84px; margin-bottom: 20px; }
  .front__name {
    color: var(--blue);
    font-weight: 700;
    font-size: 27px;
    letter-spacing: 1px;
    text-transform: uppercase;
  }
  .front__specialties {
    font-family: "Raleway", Arial, sans-serif;
    font-weight: 300;
    color: var(--grey);
    font-size: 18px;
    letter-spacing: 3px;
    text-transform: uppercase;
    margin-top: 2px;
  }
  .front__tagline {
    color: var(--blue);
    font-weight: 600;
    font-size: 13.5px;
    margin-top: 10px;
  }
</style>
</head>
<body>
  <section class="card card--contact">
    <div class="brand-block">
      <span class="brand-mark"></span>
      <span class="brand-block__name">Brush Of Heartland</span>
    </div>
    <div class="contact-block">
      <p class="contact-block__name">Marlene</p>
      <ul class="contact-list">
        <li>
          <svg viewBox="0 0 24 24" aria-hidden="true"><path d="M6.6 10.8a15.1 15.1 0 0 0 6.6 6.6l2.2-2.2c.3-.3.7-.4 1-.2 1.1.4 2.3.6 3.6.6.6 0 1 .4 1 1V20c0 .6-.4 1-1 1A17 17 0 0 1 3 4c0-.6.4-1 1-1h3.5c.6 0 1 .4 1 1 0 1.3.2 2.5.6 3.6.1.3 0 .7-.2 1z"/></svg>
          0491-635-172
        </li>
        <li>
          <svg viewBox="0 0 24 24" aria-hidden="true"><path d="M2 5h20v14H2zm2 2v.5l8 5 8-5V7l-8 5z"/></svg>
          mtorvan@quillnet.com.au
        </li>
        <li>
          <span class="social-square"></span>
          facenook.example.au/Brush Of Heartland
        </li>
      </ul>
    </div>
  </section>

  <section class="card card--front">
    <span class="brand-mark"></span>
    <h1 class="front__name">Brush Of Heartland</h1>
    <p class="front__specialties">Rustic, Provincial &amp; Alpine</p>
    <p class="front__tagline">Themed Furniture &amp; Homewares</p>
  </section>
</body>
</html>
```